Lantern Business Cards

Need business cards for my employees at my restaurant.

Needs to include:
Our Logo
Lantern Bowls & Brews
Name: Nora Pettigrew
Title : Owner
Address: 487 Mirella Ave. Lake Havasu City, AZ 86519
Web: www.lanternkestrel.com
Phone: 928-555-0147
Cell: 928-555-0192
Email: info@lanternkestrel.com

```html
<!DOCTYPE html>
<html lang="en">
<head>
<meta charset="utf-8">
<title>Lantern Bowls &amp; Brews – Business Cards</title>
<link href="https://fonts.googleapis.com/css2?family=Roboto:wght@400;500;700&display=swap" rel="stylesheet">
<style>
  :root {
    --backdrop: #1c1c1c;
    --card: #ffffff;
    --brand-red: #c42131;
    --accent-red: #e8303c;
    --ink: #1d1d1d;
    --soft-grey: #ececec;
  }
  * { margin: 0; padding: 0; box-sizing: border-box; }
  html, body { width: 1200px; height: 1059px; overflow: hidden; }
  body {
    background: var(--backdrop);
    font-family: "Roboto", Arial, sans-serif;
    color: var(--ink);
    position: relative;
  }
  .card {
    position: absolute;
    background: var(--card);
    border-radius: 28px;
    overflow: hidden;
  }
  .card--front { left: 256px; top: 95px; width: 701px; height: 401px; }
  .card--back  { left: 231px; top: 534px; width: 719px; height: 410px; }

  .brand-mark {
    position: absolute;
    display: flex;
    align-items: center;
    gap: 12px;
    color: var(--brand-red);
    font-weight: 700;
    line-height: 1.05;
  }
  .brand-mark__dot {
    flex: none;
    border-radius: 50%;
    background: var(--brand-red);
  }
  .card--front .brand-mark { left: 40px; top: 60px; font-size: 34px; }
  .card--front .brand-mark__dot { width: 40px; height: 40px; }

  .card--back .brand-mark {
    left: 0; right: 0; top: 160px;
    justify-content: center;
    font-size: 54px;
    gap: 18px;
  }
  .card--back .brand-mark__dot { width: 60px; height: 60px; }

  .holder {
    position: absolute;
    right: 30px; top: 30px;
    text-align: right;
  }
  .holder__name { color: var(--accent-red); font-size: 27px; font-weight: 500; letter-spacing: -0.3px; }
  .holder__title { font-size: 18px; margin-top: 4px; }
  .holder-bar {
    position: absolute;
    right: 0; top: 40px;
    width: 10px; height: 42px;
    background: var(--accent-red);
  }

  .address {
    position: absolute;
    left: 36px; top: 200px;
    font-size: 19px; line-height: 24px;
  }
  .contacts {
    position: absolute;
    left: 36px; top: 258px;
    list-style: none;
    font-size: 19px;
  }
  .contacts li {
    display: flex; align-items: center;
    height: 31px;
  }
  .contacts svg { width: 18px; height: 18px; margin-right: 12px; fill: var(--accent-red); }

  .corner-emblem {
    position: absolute;
    right: -8px; bottom: -12px;
    width: 222px; height: 222px;
    border-radius: 50%;
    background: var(--soft-grey);
  }
</style>
</head>
<body>
  <section class="card card--front">
    <div class="brand-mark">
      <span class="brand-mark__dot"></span>
      <span>Lantern<br>Bowls &amp; Brews</span>
    </div>

    <div class="holder">
      <p class="holder__name">Nora Pettigrew</p>
      <p class="holder__title">Owner</p>
    </div>
    <span class="holder-bar"></span>

    <p class="address">487 Mirella Ave. Lake<br>Havasu City, AZ 86519</p>

    <ul class="contacts">
      <li>
        <svg viewBox="0 0 24 24" aria-hidden="true"><path d="M6.6 10.8a15.1 15.1 0 0 0 6.6 6.6l2.2-2.2a1 1 0 0 1 1-.25 11.4 11.4 0 0 0 3.6.57 1 1 0 0 1 1 1V20a1 1 0 0 1-1 1A17 17 0 0 1 3 4a1 1 0 0 1 1-1h3.5a1 1 0 0 1 1 1c0 1.25.2 2.45.57 3.57a1 1 0 0 1-.25 1z"/></svg>
        928-555-0147
      </li>
      <li>
        <svg viewBox="0 0 24 24" aria-hidden="true"><path d="M7 1h10a2 2 0 0 1 2 2v18a2 2 0 0 1-2 2H7a2 2 0 0 1-2-2V3a2 2 0 0 1 2-2zm0 3v14h10V4zm5 15.2a1.2 1.2 0 1 0 0 2.4 1.2 1.2 0 0 0 0-2.4z"/></svg>
        928-555-0192
      </li>
      <li>
        <svg viewBox="0 0 24 24" aria-hidden="true"><path d="M2 5h20v14H2zm2 2v.4l8 5.2 8-5.2V7z"/></svg>
        info@lanternkestrel.com
      </li>
      <li>
        <svg viewBox="0 0 24 24" aria-hidden="true"><path d="M12 2a10 10 0 1 0 0 20 10 10 0 0 0 0-20zm-1 17.9A8 8 0 0 1 4.2 10.8L9 15.5v1a2 2 0 0 0 2 2zm6.9-2.6A2 2 0 0 0 16 16h-1v-3a1 1 0 0 0-1-1H8v-2h2a1 1 0 0 0 1-1V7h2a2 2 0 0 0 2-2v-.4a8 8 0 0 1 2.9 12.7z"/></svg>
        www.lanternkestrel.com
      </li>
    </ul>

    <span class="corner-emblem" aria-hidden="true"></span>
  </section>

  <section class="card card--back">
    <div class="brand-mark">
      <span class="brand-mark__dot"></span>
      <span>Lantern Bowls &amp; Brews</span>
    </div>
  </section>
</body>
</html>
```